Solar WiFi Charging Bench

Sales Brochure using only the colors of the Marigold Color Palette provided.
Municipal Government target customer.
Key Features are as follows:
LED Advertising display
Connection to internet (User Defined)
800W Solar
USB-A and USB-C cell phone charging ports
400ah battery backup with low voltage shutoff
Insulated for -40 Deg C
Wireless cell phone charging
Vandalism resistant.
Theft resistant

```html
<!DOCTYPE html>
<html lang="en">
<head>
<meta charset="utf-8">
<title>Solar WiFi Charging Bench – Marigold Renewables</title>
<link href="https://fonts.googleapis.com/css2?family=Montserrat:wght@400;500;700;800;900&display=swap" rel="stylesheet">
<style>
  :root{
    --backdrop:#808080;
    --paper:#ffffff;
    --brand-green:#259100;
    --brand-teal:#005a6e;
    --sky-blue:#48c8f0;
    --tick-green:#63e063;
    --text-light:#ffffff;
  }
  *{margin:0;padding:0;box-sizing:border-box}
  html,body{width:1200px;height:1200px;overflow:hidden;background:var(--backdrop)}
  body{font-family:"Montserrat",sans-serif;position:relative}
  .brochure{position:absolute;left:183px;top:59px;width:842px;height:1089px;background:var(--paper);overflow:hidden}
  .backdrop-art{position:absolute;left:0;top:0;width:842px;height:1089px}
  .headline{position:absolute;left:81px;font-weight:900;line-height:1;white-space:nowrap;letter-spacing:-0.5px}
  .headline--solar{top:29px;font-size:76px;color:var(--brand-green)}
  .headline--charging{top:103px;font-size:82px;color:var(--brand-teal)}
  .headline--bench{top:178px;font-size:101px;color:var(--brand-teal)}
  .brand{position:absolute;left:600px;top:40px;width:200px;text-align:center;color:var(--brand-teal);font-weight:800}
  .brand__dot{width:84px;height:84px;border-radius:50%;background:var(--sky-blue);margin:0 auto 14px}
  .brand__name{font-size:31px;line-height:1;letter-spacing:0.5px}
  .brand__sub{font-size:13px;letter-spacing:1.5px;margin-top:4px}
  .product-photo{position:absolute;left:54px;top:587px;width:331px;height:394px;border-radius:2px;
    background:linear-gradient(160deg,#e9ecee 0%,#c9ced2 45%,#f1f2f3 70%,#b7a08c 85%,#e4e6e8 100%)}
  .features-tab{position:absolute;left:349px;top:666px;width:400px;height:47px;background:var(--brand-green);
    border-radius:0 24px 24px 0;color:var(--text-light);font-weight:800;font-size:30px;line-height:47px;text-align:center;padding-left:24px}
  .feature-list{position:absolute;left:366px;top:707px;list-style:none;color:var(--text-light);font-size:18.5px;font-weight:500}
  .feature-list li{display:flex;align-items:center;height:27.4px;white-space:nowrap}
  .feature-list svg{width:16px;height:16px;margin-right:12px;flex:none}
  .footer-link{position:absolute;left:76px;top:1038px;display:flex;align-items:center;color:var(--brand-teal);font-weight:800;font-size:36px;line-height:48px;white-space:nowrap}
  .footer-link svg{width:28px;height:28px;margin-right:12px}
</style>
</head>
<body>
<main class="brochure">
  <svg class="backdrop-art" viewBox="0 0 842 1089" aria-hidden="false">
    <defs>
      <linearGradient id="sceneTone" x1="0" y1="0" x2="0" y2="1">
        <stop offset="0" stop-color="#ffffff"/>
        <stop offset="0.3" stop-color="#dfe3e0"/>
        <stop offset="0.55" stop-color="#a9b7a0"/>
        <stop offset="0.75" stop-color="#9c9a7a"/>
        <stop offset="1" stop-color="#8a7b5e"/>
      </linearGradient>
    </defs>
    <path role="img" aria-label="Photo of the solar charging bench installed on grass beside a parking lot and building" d="M0,170 L842,170 L842,453 Q760,580 536,668 L292,668 Q110,600 0,397 Z" fill="url(#sceneTone)"/>
    <path d="M0,397 Q110,600 292,668 L0,668 Z" fill="var(--sky-blue)"/>
    <path d="M842,453 Q760,580 536,668 L842,668 Z" fill="var(--sky-blue)"/>
    <path d="M0,397 Q110,600 292,668" fill="none" stroke="var(--brand-green)" stroke-width="7"/>
    <path d="M842,453 Q760,580 536,668" fill="none" stroke="var(--brand-green)" stroke-width="7"/>
    <path d="M0,628 C140,640 300,672 440,668 C560,664 620,636 700,640 C760,643 800,660 842,668 L842,1031 L0,1031 Z" fill="var(--brand-teal)"/>
  </svg>

  <h1>
    <div class="headline headline--solar">SOLAR WIFI</div>
    <div class="headline headline--charging">CHARGING</div>
    <div class="headline headline--bench">BENCH</div>
  </h1>

  <div class="brand">
    <div class="brand__dot"></div>
    <div class="brand__name">MARIGOLD</div>
    <div class="brand__sub">RENEWABLES</div>
  </div>

  <div class="product-photo" role="img" aria-label="Photo of the charging bench with curved canopy, wooden seat and advertising screen"></div>

  <div class="features-tab">Key Features</div>

  <ul class="feature-list">
    <li><svg viewBox="0 0 16 16"><path d="M2 8.5l4 4L14 3.5" fill="none" stroke="var(--tick-green)" stroke-width="2.6" stroke-linecap="round" stroke-linejoin="round"/></svg>LED Advertising display</li>
    <li><svg viewBox="0 0 16 16"><path d="M2 8.5l4 4L14 3.5" fill="none" stroke="var(--tick-green)" stroke-width="2.6" stroke-linecap="round" stroke-linejoin="round"/></svg>Connection to internet (User Defined)</li>
    <li><svg viewBox="0 0 16 16"><path d="M2 8.5l4 4L14 3.5" fill="none" stroke="var(--tick-green)" stroke-width="2.6" stroke-linecap="round" stroke-linejoin="round"/></svg>800W Solar</li>
    <li><svg viewBox="0 0 16 16"><path d="M2 8.5l4 4L14 3.5" fill="none" stroke="var(--tick-green)" stroke-width="2.6" stroke-linecap="round" stroke-linejoin="round"/></svg>USB-A and USB-C cell phone charging ports</li>
    <li><svg viewBox="0 0 16 16"><path d="M2 8.5l4 4L14 3.5" fill="none" stroke="var(--tick-green)" stroke-width="2.6" stroke-linecap="round" stroke-linejoin="round"/></svg>400ah battery backup with low voltage shutoff</li>
    <li><svg viewBox="0 0 16 16"><path d="M2 8.5l4 4L14 3.5" fill="none" stroke="var(--tick-green)" stroke-width="2.6" stroke-linecap="round" stroke-linejoin="round"/></svg>Insulated for -40 Deg C</li>
    <li><svg viewBox="0 0 16 16"><path d="M2 8.5l4 4L14 3.5" fill="none" stroke="var(--tick-green)" stroke-width="2.6" stroke-linecap="round" stroke-linejoin="round"/></svg>Wireless cell phone charging</li>
    <li><svg viewBox="0 0 16 16"><path d="M2 8.5l4 4L14 3.5" fill="none" stroke="var(--tick-green)" stroke-width="2.6" stroke-linecap="round" stroke-linejoin="round"/></svg>Vandalism resistant</li>
    <li><svg viewBox="0 0 16 16"><path d="M2 8.5l4 4L14 3.5" fill="none" stroke="var(--tick-green)" stroke-width="2.6" stroke-linecap="round" stroke-linejoin="round"/></svg>Theft resistant</li>
  </ul>

  <div class="footer-link">
    <svg viewBox="0 0 28 28"><g fill="none" stroke="var(--brand-teal)" stroke-width="2.6"><circle cx="14" cy="14" r="11.5"/><ellipse cx="14" cy="14" rx="5" ry="11.5"/><path d="M2.5 14h23M4.5 8h19M4.5 20h19"/></g></svg>
    www.marigoldrenewables.com
  </div>
</main>
</body>
</html>
```